Property investor needs a business card with logo

I need a business card for a UK based business called 'Bright Gate Homes'. I buy houses quickly that is either hard to sell or people have been having trouble to sell. I then create the opportunity for people to buy houses that normally can't. This could be because they have little or no deposit saved up or they don't qualify for a mortgage. The design is to be bright so that it stands out but non threatening and basic. Yellow for the bass colour. The logo to be very simple and represent a house. It could include words like "cant sell? I'll buy it!!" or "Need a quick sale? Let me help" or something as simple as "I buy houses!!" The final design should communicate that I am not some big corporate person that is better that them, but someone that is just a person trying to help them with their situation. with a picture of me with the background removed.
Target Market(s)
Normal everyday people
Industry/Entity Type
Business
Contact Information for Business Card
Gareth Pellingham
07845619027
brightgatehomes@mailbox.example
Font styles to use
Other font styles liked:
- something that looks hand written
Look and feel
Each slider illustrates characteristics of the customer's brand and the style your logo design should communicate.

```html
<!DOCTYPE html>
<html lang="en">
<head>
<meta charset="utf-8">
<title>Bright Gate Homes – Business Card</title>
<link rel="stylesheet" href="https://fonts.googleapis.com/css2?family=Didact+Gothic&display=swap">
<style>
  :root {
    --backdrop: #e6e3dd;
    --card-front: #f8f6e7;
    --card-back: #dccfb2;
    --ink: #1e1e1e;
    --name-blue: #2a79c2;
    --brand-magenta: #c8127a;
    --photo-cream: #f3eedc;
    --photo-yellow: #e4c63a;
    --photo-pink: #d54a8e;
    --photo-blue: #3aa1d8;
    --photo-dark: #23263a;
  }
  * { margin: 0; padding: 0; box-sizing: border-box; }
  html, body {
    width: 1200px; height: 1200px; overflow: hidden;
    background: var(--backdrop);
    font-family: "Didact Gothic", sans-serif;
  }
  .sheet {
    width: 1200px; height: 1200px;
    display: flex; flex-direction: column;
    align-items: center; justify-content: center; gap: 64px;
  }
  .card {
    position: relative;
    width: 900px; height: 514px;
    box-shadow: 0 6px 18px rgba(0,0,0,.18);
    overflow: hidden;
  }
  .card--front { background: var(--card-front); }
  .card--back { background: var(--card-back); display: flex; align-items: center; justify-content: center; }

  .brand {
    display: flex; align-items: center; gap: 12px;
    color: var(--ink);
    font-size: 28px; letter-spacing: .3px; white-space: nowrap;
  }
  .brand__square { width: 32px; height: 32px; background: var(--brand-magenta); flex: none; }
  .card--front .brand { position: absolute; left: 64px; top: 176px; }

  .portrait {
    position: absolute; right: 0; top: 0;
    width: 490px; height: 322px;
    background:
      radial-gradient(ellipse 38% 60% at 38% 72%, var(--photo-dark) 0 60%, transparent 62%),
      linear-gradient(135deg, var(--photo-yellow) 0%, var(--photo-pink) 35%, var(--photo-cream) 55%, var(--photo-blue) 80%, var(--photo-yellow) 100%);
  }

  .contact { position: absolute; left: 112px; top: 300px; color: var(--ink); }
  .contact__name { color: var(--name-blue); font-size: 28px; margin-bottom: 22px; }
  .contact__line { font-size: 22px; letter-spacing: 1px; margin-bottom: 18px; }
</style>
</head>
<body>
  <main class="sheet">
    <section class="card card--front">
      <div class="brand">
        <span class="brand__square"></span>
        <span class="brand__name">bright gate homes</span>
      </div>
      <div class="portrait" role="img" aria-label="Portrait of Gareth Pellingham in front of a colourful pattern of small painted houses"></div>
      <div class="contact">
        <p class="contact__name">Gareth Pellingham</p>
        <p class="contact__line">0784.5619.027</p>
        <p class="contact__line">brightgatehomes@mailbox.example</p>
      </div>
    </section>

    <section class="card card--back">
      <div class="brand">
        <span class="brand__square"></span>
        <span class="brand__name">bright gate homes</span>
      </div>
    </section>
  </main>
</body>
</html>
```